Camp Flyer

We are hosting a camp over the last week of October. We would like a high res file for a flyer that we can get printed. Double sided would be great but i would also like a version that is only 1 side that can be sent out via email to our database and also posted on our social media platforms.

The text that should be included
Mid Term Camp
26th - 30th of October
9am - 3pm
800 aed

Let your star shine bright!
Daily speech and confidence building classes, music & movement, song, arts & crafts, fine motor development and right brain training!

Special performance of the Patchwork Fox from Quillby Theatre Group (Wednesday).

Pixelnook Camp photo gallery updated daily!

Limited Spaces Available

register@wrenbloom.ae or 043192764/ 0529316472
www.wrenbloom.ae

- I have a larger file of this photo it would just not allow me to attach the large file to this brief.

For details on the theatre show please look at www.quillbytheatre.com - please use their patchwork fox and logo

```html
<!DOCTYPE html>
<html lang="en">
<head>
<meta charset="utf-8">
<title>Mid Term Camp Flyer</title>
<link rel="stylesheet" href="https://fonts.googleapis.com/css2?family=Lilita+One&family=Open+Sans:wght@400;700;800&family=Chewy&family=Gochi+Hand&display=swap">
<style>
  :root {
    --page: #ece7e1;
    --pink: #e5007d;
    --pink-deep: #c8006b;
    --green: #8cc63f;
    --yellow: #ffe000;
    --blue: #1fa6d8;
    --cyan: #29b3de;
    --sky: #cfe9f8;
    --sky-deep: #8fcbef;
    --orange: #e98b1c;
    --ink: #1b1b1b;
    --white: #ffffff;
  }
  * { box-sizing: border-box; margin: 0; padding: 0; }
  html, body { width: 964px; height: 1200px; overflow: hidden; background: var(--page); }
  .flyer {
    position: absolute; left: 70px; top: 22px; width: 824px; height: 1155px;
    background: repeating-linear-gradient(90deg, var(--pink) 0 3px, #ea1689 3px 5px);
    overflow: hidden;
    font-family: "Open Sans", Arial, sans-serif;
  }
  .flyer-shapes { position: absolute; inset: 0; }
  .title {
    position: absolute; left: 0; width: 100%; text-align: center;
    font-family: "Lilita One", "Arial Black", sans-serif; color: var(--green);
    -webkit-text-stroke: 3px var(--pink-deep); paint-order: stroke fill;
    text-shadow: 0 0 0 var(--white), 3px 3px 0 var(--white), -3px -3px 0 var(--white), 3px -3px 0 var(--white), -3px 3px 0 var(--white);
    line-height: 1;
  }
  .title-top { top: 44px; font-size: 72px; letter-spacing: 1px; }
  .title-main { top: 106px; font-size: 108px; }
  .dates { position: absolute; top: 252px; width: 100%; text-align: center; font-weight: 800; font-size: 33px; color: var(--ink); }
  .rule { position: absolute; left: 250px; width: 324px; border-top: 2px dotted var(--ink); }
  .rule-upper { top: 292px; }
  .rule-lower { top: 334px; }
  .hours { position: absolute; top: 299px; width: 100%; text-align: center; font-weight: 700; font-size: 22px; color: var(--ink); }
  .tagline { position: absolute; top: 344px; width: 100%; text-align: center; font-family: "Chewy", cursive; font-size: 44px; color: var(--pink); }
  .details { position: absolute; left: 130px; width: 564px; text-align: center; font-size: 16px; line-height: 19px; color: var(--ink); }
  .details-classes { top: 396px; }
  .details-show { top: 458px; }
  .band {
    position: absolute; left: 0; top: 990px; width: 100%; height: 38px; background: var(--cyan);
    color: var(--white); font-weight: 700; font-size: 17px; line-height: 38px; padding-left: 186px;
  }
  .brand {
    position: absolute; left: 34px; top: 932px; width: 156px; height: 166px;
    background: var(--white); border: 4px solid var(--cyan); border-radius: 14px;
    display: flex; flex-direction: column; align-items: center; justify-content: space-between; padding: 20px 8px 12px;
  }
  .brand-name { font-weight: 800; font-size: 22px; color: var(--blue); text-align: center; line-height: 1.1; margin-top: 20px; }
  .brand-tag { width: 100%; background: var(--blue); color: var(--white); font-size: 11px; font-weight: 700; text-align: center; padding: 5px 2px; border-radius: 3px; }
  .spaces {
    position: absolute; left: 590px; top: 857px; width: 148px; height: 148px; border-radius: 50%;
    background: var(--yellow); border: 2px dotted var(--ink); outline: 5px solid var(--yellow);
    display: flex; align-items: center; justify-content: center; text-align: center;
    font-family: "Gochi Hand", cursive; font-size: 25px; line-height: 1.05; color: var(--ink);
    transform: rotate(-12deg);
  }
  .contact { position: absolute; right: 18px; text-align: right; color: var(--white); font-weight: 700; font-size: 17px; }
  .contact-web { top: 1072px; }
  .contact-mail { top: 1102px; }
</style>
</head>
<body>
<main class="flyer">
  <svg class="flyer-shapes" viewBox="0 0 824 1155" aria-hidden="true">
    <defs>
      <radialGradient id="skyGlow" cx="0.5" cy="0.35" r="0.7">
        <stop offset="0" stop-color="#ffffff"/>
        <stop offset="0.5" stop-color="var(--sky)"/>
        <stop offset="1" stop-color="var(--sky-deep)"/>
      </radialGradient>
      <linearGradient id="sceneTone" x1="0" y1="0" x2="0" y2="1">
        <stop offset="0" stop-color="#d7ecfa"/>
        <stop offset="0.45" stop-color="#e9c9b8"/>
        <stop offset="1" stop-color="#c9384a"/>
      </linearGradient>
    </defs>
    <path class="backing-edge" d="M80 120 C60 300 40 520 70 700 L60 980 L790 980 L800 700 C770 520 780 300 760 130 Z" fill="var(--orange)"/>
    <path class="sky-panel" d="M96 96 C200 150 320 150 412 120 C500 150 620 150 740 100 C760 300 770 520 760 720 L762 960 L92 960 L92 720 C70 520 80 300 96 96 Z" fill="url(#skyGlow)" stroke="var(--white)" stroke-width="10"/>
    <rect class="scene" role="img" aria-label="Photo of children in party costumes with a patchwork fox character and balloons" x="60" y="560" width="740" height="430" rx="30" fill="url(#sceneTone)"/>
    <g class="bubbles">
      <circle cx="112" cy="131" r="48" fill="var(--blue)" stroke="var(--white)" stroke-width="5"/>
      <circle cx="163" cy="75" r="32" fill="var(--yellow)" stroke="var(--white)" stroke-width="5"/>
      <circle cx="80" cy="86" r="12" fill="var(--green)" stroke="var(--white)" stroke-width="3"/>
      <circle cx="653" cy="115" r="51" fill="var(--green)" stroke="var(--white)" stroke-width="5"/>
      <circle cx="624" cy="158" r="32" fill="var(--yellow)" stroke="var(--white)" stroke-width="5"/>
      <circle cx="722" cy="188" r="35" fill="var(--blue)" stroke="var(--white)" stroke-width="5"/>
      <circle cx="787" cy="464" r="35" fill="var(--yellow)" stroke="var(--white)" stroke-width="5"/>
      <circle cx="795" cy="560" r="19" fill="var(--blue)" stroke="var(--white)" stroke-width="4"/>
      <circle cx="53" cy="582" r="22" fill="var(--green)" stroke="var(--white)" stroke-width="4"/>
      <circle cx="120" cy="614" r="35" fill="var(--yellow)" stroke="var(--white)" stroke-width="5"/>
      <circle cx="77" cy="672" r="51" fill="var(--blue)" stroke="var(--white)" stroke-width="5"/>
      <circle cx="778" cy="707" r="32" fill="var(--blue)" stroke="var(--white)" stroke-width="5"/>
      <circle cx="771" cy="768" r="45" fill="var(--green)" stroke="var(--white)" stroke-width="5"/>
      <circle cx="752" cy="972" r="35" fill="var(--green)" stroke="var(--white)" stroke-width="5"/>
      <circle cx="632" cy="869" r="16" fill="var(--pink)" stroke="var(--white)" stroke-width="4"/>
    </g>
  </svg>

  <h1 class="title title-top">MID TERM</h1>
  <div class="title title-main">CAMP</div>
  <p class="dates">26th - 30th of October</p>
  <div class="rule rule-upper"></div>
  <p class="hours">9am - 3pm • 800 aed</p>
  <div class="rule rule-lower"></div>
  <h2 class="tagline">Let your star shine bright!</h2>
  <p class="details details-classes">Daily speech and confidence building classes, music &amp; movement, song, arts &amp; crafts, fine motor development and right brain training!</p>
  <p class="details details-show">Special performance of the Patchwork Fox from Quillby Theatre Group (Wednesday).</p>

  <div class="band">Pixelnook Camp photo gallery updated daily!</div>
  <div class="brand">
    <span class="brand-name">Wren Bloom</span>
    <span class="brand-tag">Accelerated Learning Centre</span>
  </div>
  <div class="spaces">Limited<br>Spaces<br>Available</div>
  <p class="contact contact-web">www.wrenbloom.ae</p>
  <p class="contact contact-mail">register@wrenbloom.ae or 043192764/ 0529316472</p>
</main>
</body>
</html>
```